" Trabalho de forma autônoma como Coach Executivo. O Coaching executivo pode ser contratado tanto por PJ como por PF. São sessões / reuniões nas quais trabalhamos de forma individual para desenvolvimento da pessoa - desenvolvimento de habilidades, autoconsciência dos pontos fortes e pontos a serem desenvolvidos, para que a pessoa desempenhe seu máximo em sua carreira profissional e atinja o sucesso que ela determinou. O foco do trabalho é o desenvolvimento de competências / habilidades para ela desempenhar seu trabalho e se desenvolver em sua carreira profissional com excelência. Também tem o foco, no Coaching de Carreira, na redefinição dos rumos profissionais de uma pessoa. Discussão de possibilidades de caminhos a serem seguidos e uma reflexão do que aconteceu até o momento. Em ambos os casos, é um processo de autoreflexão mas que já parte para a AÇÃO. Não tem nada de estático, só ficar pensando e divagando em ideias. O ponto é fazer com que a pessoa se mova, saia do lugar, vá buscar seus objetivos. Esse apoio durante o processo também é dado para que a ação efetivamente aconteça. "

```html
<!DOCTYPE html>
<html lang="pt-BR">
<head>
<meta charset="utf-8">
<title>Helena Morita Coaching — Cartões de visita</title>
<link rel="stylesheet" href="https://fonts.googleapis.com/css2?family=Cinzel:wght@400&family=Arimo:wght@400;700&display=swap">
<style>
  :root {
    --stage: #1e1e1f;
    --card: #2c2d30;
    --accent: #3cb9d9;
    --ink: #ffffff;
  }
  * { margin: 0; padding: 0; box-sizing: border-box; }
  html, body { width: 1200px; height: 1200px; overflow: hidden; background: var(--stage); }
  .stage { position: relative; width: 1200px; height: 1200px; }

  .card { position: absolute; left: 286px; width: 628px; height: 350px; background: var(--card); overflow: hidden; }
  .card--front { top: 233px; }
  .card--back { top: 619px; }

  .brand-mark { position: absolute; left: 282px; top: 92px; width: 64px; height: 64px; border-radius: 50%; background: var(--accent); }
  .brand-name { position: absolute; left: 0; right: 0; text-align: center; font-family: "Cinzel", serif; color: var(--ink); font-weight: 400; }
  .brand-name--front { top: 190px; font-size: 44px; letter-spacing: 1px; }
  .brand-tag { position: absolute; left: 0; right: 0; text-align: center; font-family: "Cinzel", serif; color: var(--ink); font-weight: 400; }
  .brand-tag--front { top: 254px; font-size: 13px; letter-spacing: 9px; padding-left: 9px; }

  .front-tab { position: absolute; left: 81px; top: 326px; width: 461px; height: 30px; background: var(--accent); border-radius: 12px 12px 0 0; }

  .back-band { position: absolute; left: 0; top: 58px; width: 100%; height: 24px; background: var(--accent); }
  .back-mark { position: absolute; left: 120px; top: 39px; width: 62px; height: 62px; border-radius: 50%; background: var(--accent); border: 2px solid #2a8fab; }
  .back-name { position: absolute; left: 333px; top: 94px; width: 245px; text-align: center; font-family: "Cinzel", serif; color: var(--ink); }
  .back-name .name { display: block; font-size: 22px; line-height: 1; }
  .back-name .tag { display: block; font-size: 6px; letter-spacing: 4px; margin-top: 2px; }

  .contact-list { position: absolute; right: 36px; top: 158px; list-style: none; }
  .contact-item { display: flex; align-items: center; justify-content: flex-end; gap: 22px; height: 19px; margin-bottom: 30px; font-family: "Arimo", sans-serif; font-weight: 700; font-size: 18px; color: var(--ink); }
  .contact-item:nth-child(2) { margin-bottom: 34px; }
  .contact-icon { width: 16px; height: 16px; flex: none; }
</style>
</head>
<body>
<main class="stage">
  <section class="card card--front" aria-label="Frente do cartão">
    <div class="brand-mark"></div>
    <h1 class="brand-name brand-name--front">Helena Morita</h1>
    <p class="brand-tag brand-tag--front">COACHING</p>
    <div class="front-tab"></div>
  </section>

  <section class="card card--back" aria-label="Verso do cartão">
    <div class="back-band"></div>
    <div class="back-mark"></div>
    <div class="back-name">
      <span class="name">HELENA MORITA</span>
      <span class="tag">COACHING</span>
    </div>
    <ul class="contact-list">
      <li class="contact-item">
        <span>contato@helenamorita.com.br</span>
        <svg class="contact-icon" viewBox="0 0 16 16" aria-hidden="true">
          <rect x="1" y="3" width="14" height="10" fill="#fff"/>
          <path d="M1 3 L8 9 L15 3" fill="none" stroke="#2c2d30" stroke-width="1.4"/>
        </svg>
      </li>
      <li class="contact-item">
        <span>11 98765-4321</span>
        <svg class="contact-icon" viewBox="0 0 16 16" aria-hidden="true">
          <path d="M1 6 Q8 1 15 6 L13 8 L11 6.5 L11 5 Q8 4 5 5 L5 6.5 L3 8 Z" fill="#fff"/>
          <rect x="3" y="9" width="10" height="5" rx="1" fill="#fff"/>
        </svg>
      </li>
      <li class="contact-item">
        <span>perfil.exemplo.com/helena-morita</span>
        <svg class="contact-icon" viewBox="0 0 16 16" aria-hidden="true">
          <circle cx="8" cy="8" r="6" fill="#fff"/>
        </svg>
      </li>
    </ul>
  </section>
</main>
</body>
</html>
```